" Nossa empresa esse ano faz 15 anos de vida. Durante a Pandemia, fechamos o escritório e agora estamos reabrindo. Atuamos com inúmeros clientes, tanto governo, como empresas privadas nas nossas áreas de atuação. "

```html
<!DOCTYPE html>
<html lang="pt-BR">
<head>
<meta charset="utf-8">
<title>Nexora – Painel de Parede</title>
<link rel="stylesheet" href="https://fonts.googleapis.com/css2?family=Montserrat:wght@400;500;700;800&display=swap">
<style>
  :root {
    --page: #ffffff;
    --wall-dark: #3a3a3a;
    --wall-mid: #4a4a4a;
    --wall-light: #5a5a5a;
    --seam: rgba(255,255,255,0.18);
    --label: #ffffff;
    --dash: #b8c94a;
    --icon: #c9d66a;
    --brand-red: #b51f24;
    --brand-green: #4a9a2e;
    --panel-white: #f6f6f6;
    --tile: #e4e4e4;
  }
  * { margin: 0; padding: 0; box-sizing: border-box; }
  html, body { width: 1200px; height: 1200px; overflow: hidden; background: var(--page); }
  body { font-family: "Montserrat", Arial, sans-serif; position: relative; }

  .mural {
    position: absolute; left: 60px; top: 353px; width: 1085px; height: 499px;
    display: flex; box-shadow: 0 2px 6px rgba(0,0,0,0.15);
  }
  .mural__dark {
    position: relative; width: 869px; height: 100%;
    background: radial-gradient(ellipse at 45% 40%, var(--wall-light) 0%, var(--wall-mid) 45%, var(--wall-dark) 100%);
    overflow: hidden;
  }
  .mural__light {
    position: relative; flex: 1; height: 100%; background: var(--panel-white);
    border-left: 1px solid #ddd; overflow: hidden;
  }
  .seam { position: absolute; top: 0; bottom: 0; width: 1px; background: var(--seam); }

  .hero-visual {
    position: absolute; left: 264px; top: 31px; width: 372px; height: 468px;
    background: linear-gradient(180deg, rgba(140,40,40,0.55) 0%, rgba(110,60,50,0.45) 55%, rgba(150,110,90,0.35) 100%);
  }

  .connectors { position: absolute; inset: 0; }

  .area__icon {
    position: absolute; width: 28px; height: 28px;
    border: 2px solid var(--icon); border-radius: 50%;
  }
  .area__label {
    position: absolute; color: var(--label); font-size: 18px; font-weight: 500;
    letter-spacing: 0.5px; line-height: 22px; white-space: nowrap;
  }

  .brand { position: absolute; display: flex; align-items: center; gap: 10px; }
  .brand__mark { width: 26px; height: 26px; background: #ffffff; }
  .brand__text { display: flex; flex-direction: column; }
  .brand__name { font-weight: 800; color: #ffffff; font-size: 30px; line-height: 1; }
  .brand__tag { font-size: 10px; color: #ffffff; font-weight: 500; margin-top: 3px; }

  .brand--panel { left: 0; right: 0; top: 120px; flex-direction: column; align-items: center; gap: 4px; }
  .brand--panel .brand__name { color: var(--brand-red); font-size: 42px; }
  .brand--panel .brand__tag { color: var(--brand-green); font-size: 11px; letter-spacing: 1px; }

  .panel-decor {
    position: absolute; right: 0; bottom: 0; width: 200px; height: 250px;
    background: linear-gradient(135deg, rgba(228,228,228,0) 0%, rgba(228,228,228,0.6) 45%, var(--tile) 100%);
  }
</style>
</head>
<body>
  <section class="mural">
    <div class="mural__dark">
      <span class="seam" style="left:214px"></span>
      <span class="seam" style="left:434px"></span>
      <span class="seam" style="left:650px"></span>

      <div class="hero-visual" role="img" aria-label="Foto: mão aberta segurando um cubo de peças vermelhas e verdes"></div>

      <svg class="connectors" width="869" height="499" viewBox="0 0 869 499">
        <g fill="none" stroke="var(--dash)" stroke-width="1.5" stroke-dasharray="5 4">
          <polyline points="205,89 270,89 300,108"/>
          <polyline points="195,223 268,223 298,240"/>
          <polyline points="228,362 268,362 298,340"/>
          <polyline points="540,82 562,60 582,60"/>
          <polyline points="565,214 592,194 638,194"/>
          <polyline points="598,340 622,326 662,326"/>
        </g>
      </svg>

      <span class="area__icon" style="left:111px; top:38px;"></span>
      <span class="area__label" style="left:55px; top:78px;">CONSULTORIA</span>

      <span class="area__icon" style="left:38px; top:172px;"></span>
      <span class="area__label" style="left:20px; top:212px;">CONHECIMENTO</span>

      <span class="area__icon" style="left:104px; top:312px;"></span>
      <span class="area__label" style="left:106px; top:351px;">EDUCAÇÃO</span>

      <span class="area__icon" style="left:680px; top:16px;"></span>
      <span class="area__label" style="left:592px; top:49px;">INOVAÇÃO</span>

      <span class="area__icon" style="left:725px; top:150px;"></span>
      <span class="area__label" style="left:648px; top:183px;">PROJETOS</span>

      <span class="area__icon" style="left:701px; top:283px;"></span>
      <span class="area__label" style="left:672px; top:315px;">RH</span>

      <div class="brand" style="left:24px; top:410px;">
        <span class="brand__mark"></span>
        <span class="brand__text">
          <span class="brand__name">Nexora</span>
          <span class="brand__tag">Educação e Projetos</span>
        </span>
      </div>
    </div>

    <div class="mural__light">
      <div class="brand brand--panel">
        <span class="brand__name">Nexora</span>
        <span class="brand__tag">Educação e Projetos</span>
      </div>
      <div class="panel-decor" role="img" aria-label="Decoração suave em tons de cinza claro"></div>
    </div>
  </section>
</body>
</html>
```